Natural Skincare Product Labels Design

We are looking for a designer to create elegant but quirky, functional product labels for our natural skincare range.
The labels must reflect our brand’s values of simplicity, luxury, and the natural, handmade essence of our products.
https://www.pictogrove.com/marvellaskincare
1. Key Details
Packaging Dimensions
Container Types: Transparent jars.
Sizes for Body Products:
Diameter: 64mm–68mm.
Heights: 80mm, 88mm, and 97mm (lid height: 15mm).
Sizes for Face Creams:
Diameter: 60mm.
Height: 50mm (lid height: 15mm).
Label Fit: For body products, ideally one label size to fit all jar sizes.
For the smaller face cream jars, a separate, tailored label is required.
2. Label Placement
Options include a wrapped-around label or a combination of wrapped-around and top-of-jar elements.
Transparent jars mean the label must leave space for the product to be visible (e.g., partial wrap or cutout areas).
3. Content Requirements
Product Name: Prominently displayed.
Ingredient List: Dedicated space required.
Disclaimer/Usage Instructions: Include space for this information.
4. Design Goals
Look & Feel: Simple, upmarket, and natural, with a handmade essence.
Logo Usage: Our logo is finalized and available in gold, black, and white variants. Use Josefin Bold font for the logo if adjustments are required.
Color Palette: Neutral tones (e.g., whites, blacks, golds) are preferred, with flexibility for subtle pops of color tied to each product’s main ingredient.
5. Imagery
Open to including images and colours (e.g., botanical illustrations) that highlight the main ingredient (e.g., coffee beans, turmeric root, or honeycomb). Also open to labels having a prominent colour to tie it in to the main ingredient.
Alternatively, no images can also work for a clean design.
6. Current Design Context
Our temporary design features gold leaf on top and a simple handmade side label. We’re seeking to elevate this to a more polished, cohesive design.
7. Product Line
- Body Products (Larger Jars)
Tolo Body Butter
Key Ingredients: Guarana & Cupuaçu butter (inspired by Brazil).
Note: “Tolo” is slang for “bum.”
Manuka Honey Body Butter
Key Ingredients: Manuka honey (from New Zealand) & Cupuaçu butter.
Coffee Body Scrub
Key Ingredients: Coffee and Demerara sugar.
Whipped Body Soap - Turmeric
Key Ingredients: Turmeric and Bentonite clay.
Whipped Body Soap - Banana
- Face Products (Smaller Jars)
Face Cream
Key Ingredients: Carrot Oil and Raspberry Oil.
Features natural UV protection.
Good Night Cream
Key Ingredients: Enriched with Magnesium.
Promotes relaxation and restful sleep.
8. Submission Guidelines
Flexibility: Design should allow for consistent branding across all products while accommodating the varying jar sizes and ingredient focus.
Material Considerations: Labels should complement the transparent jars and allow the product inside to remain partially visible.
Print Elements: Incorporating gold accents is a plus but should not overpower the design.
We’re excited to see your vision for a label that celebrates the natural beauty and high quality of our skincare range. Please include mockups to showcase the design in use, particularly on transparent jars of varying sizes.
women 20-50 years of age

```html
<!DOCTYPE html>
<html lang="en">
<head>
<meta charset="utf-8">
<title>Marvella Coffee Scrub Label</title>
<link href="https://fonts.googleapis.com/css2?family=Montserrat:wght@400;500&family=Mrs+Saint+Delafield&display=swap" rel="stylesheet">
<style>
  :root {
    --page: #ececec;
    --label: #ffffff;
    --ink: #111111;
    --gold: #c08a2e;
    --leaf-dark: #141414;
    --leaf-soft: rgba(20, 20, 20, 0);
  }
  * { box-sizing: border-box; margin: 0; padding: 0; }
  html, body {
    width: 1200px;
    height: 1090px;
    overflow: hidden;
    background: var(--page);
  }
  .canvas {
    position: relative;
    width: 1200px;
    height: 1090px;
  }
  .label {
    position: absolute;
    left: 100px;
    top: 328px;
    width: 1000px;
    height: 434px;
    background: var(--label);
  }
  .brand {
    position: absolute;
    left: 110px;
    top: 70px;
    display: flex;
    align-items: center;
    gap: 14px;
  }
  .brand-mark {
    width: 40px;
    height: 40px;
    border: 2px solid var(--gold);
    border-radius: 50%;
  }
  .brand-name {
    font-family: "Montserrat", sans-serif;
    font-weight: 500;
    font-size: 30px;
    letter-spacing: 5px;
    color: var(--gold);
  }
  .product-name {
    position: absolute;
    left: 150px;
    top: 178px;
    width: 350px;
    text-align: center;
    font-family: "Mrs Saint Delafield", cursive;
    font-size: 86px;
    line-height: 1;
    color: var(--ink);
  }
  .ingredients {
    position: absolute;
    left: 150px;
    top: 283px;
    width: 350px;
    text-align: center;
    font-family: "Montserrat", sans-serif;
    font-weight: 400;
    font-size: 19px;
    line-height: 26px;
    letter-spacing: 1.5px;
    text-transform: uppercase;
    color: var(--ink);
  }
  .divider {
    position: absolute;
    left: 526px;
    top: 196px;
    width: 2px;
    height: 150px;
    background: var(--ink);
  }
  .usage {
    position: absolute;
    left: 562px;
    top: 196px;
    width: 300px;
    font-family: "Montserrat", sans-serif;
    font-weight: 500;
    font-size: 14px;
    line-height: 20.5px;
    color: var(--ink);
  }
  .usage p + p { margin-top: 20px; }
  .botanical {
    position: absolute;
    background: radial-gradient(ellipse at center, var(--leaf-dark) 0%, var(--leaf-dark) 35%, var(--leaf-soft) 72%);
  }
  .botanical-top {
    left: 758px;
    top: 0;
    width: 206px;
    height: 183px;
  }
  .botanical-bottom {
    left: 29px;
    top: 321px;
    width: 124px;
    height: 113px;
  }
</style>
</head>
<body>
  <main class="canvas">
    <section class="label">
      <div class="brand">
        <span class="brand-mark"></span>
        <span class="brand-name">MARVELLA</span>
      </div>

      <h1 class="product-name">CoffeeScrub</h1>
      <p class="ingredients">Coconut butter, coffee,<br>cocoa butter, vitamin A</p>

      <div class="divider"></div>

      <div class="usage">
        <p>Extreme refreshing - Coffee Scrub is gentle formula which exfoliates the upper dead skin layer</p>
        <p>Direction: Apply a generous amount of Coffee Scrub on the clean and washed Elbows, Knees and heels.</p>
      </div>

      <div class="botanical botanical-top" role="img" aria-label="Black botanical illustration of a coffee branch with leaves and berries"></div>
      <div class="botanical botanical-bottom" role="img" aria-label="Small black illustration of coffee leaves with berries"></div>
    </section>
  </main>
</body>
</html>
```